Letterhead Design Project

Initially, we would like to review our letterheads.

Something simple which uses our corporate imagery well and is nicely balanced.

Please note that I will be following up this letter-head with some customised quote templates and similarly customisable collateral in the next few weeks.

Target Market(s)

Enterprise business

Industry/Entity Type

Quote

Requirements
Must have
• The Nexora9 logo
See www.nexora9.com.au

Our tagline "Enterprise Hosting, Messaging and Server Virtualisation"

Our website address

Ideally in our colour pallette, but will consider submissions which look fantastic and necessitate other colours.

```html
<!DOCTYPE html>
<html lang="en">
<head>
<meta charset="utf-8">
<title>Nexora9 Letterhead</title>
<link href="https://fonts.googleapis.com/css2?family=Source+Sans+3:wght@400;700&display=swap" rel="stylesheet">
<style>
  :root {
    --brand-red: #be1e2d;
    --ink: #231f20;
    --paper: #ffffff;
    --page-edge: #3a3a3a;
    --backdrop: #ffffff;
  }
  * { margin: 0; padding: 0; box-sizing: border-box; }
  html, body {
    width: 1200px;
    height: 800px;
    overflow: hidden;
    background: var(--backdrop);
    font-family: "Source Sans 3", "Myriad Pro", Arial, sans-serif;
  }
  .canvas {
    position: relative;
    width: 1200px;
    height: 800px;
  }
  .letterhead {
    position: absolute;
    left: 338px;
    top: 38px;
    width: 518px;
    height: 732px;
    background: var(--paper);
    border: 1px solid var(--page-edge);
  }
  .brand {
    position: absolute;
    right: 33px;
    top: 25px;
    display: flex;
    align-items: center;
    gap: 6px;
  }
  .brand-square {
    width: 38px;
    height: 38px;
    background: var(--brand-red);
  }
  .brand-name {
    font-weight: 700;
    font-size: 37px;
    line-height: 38px;
    color: var(--ink);
    letter-spacing: -0.5px;
  }
  .tagline {
    position: absolute;
    left: 29px;
    top: 75px;
    width: 277px;
    height: 18px;
    border: 1px solid var(--brand-red);
    color: var(--ink);
    font-size: 10.8px;
    line-height: 16px;
    letter-spacing: -0.1px;
    padding-left: 10px;
    white-space: nowrap;
    z-index: 1;
  }
  .contact-bar {
    position: absolute;
    right: 33px;
    top: 69px;
    width: 186px;
    height: 17px;
    padding: 0 4px;
    background: var(--ink);
    color: var(--paper);
    font-size: 9.4px;
    line-height: 17px;
    white-space: nowrap;
    display: flex;
    align-items: center;
    justify-content: center;
    gap: 4px;
    z-index: 2;
  }
  .contact-sep {
    width: 4px;
    height: 4px;
    background: var(--brand-red);
    display: inline-block;
    flex: none;
  }
  .corner-block {
    position: absolute;
    left: -1px;
    top: 671px;
    width: 37px;
    height: 37px;
    background: var(--brand-red);
  }
</style>
</head>
<body>
  <div class="canvas">
    <div class="letterhead">
      <div class="brand">
        <span class="brand-square"></span>
        <span class="brand-name">Nexora9</span>
      </div>
      <p class="tagline">Enterprise Hosting, Messaging and Server Virtualisation</p>
      <div class="contact-bar">
        <span class="contact-web">www.nexora9.com.au</span>
        <span class="contact-sep"></span>
        <span class="contact-email">info@nexora9.com.au</span>
      </div>
      <div class="corner-block"></div>
    </div>
  </div>
</body>
</html>
```